Website Design for Car Donations

Revise current site www.wheelsforheroes-sample.org

Sites i like:

https://www.autogiftbrigade.example

https://ridegivingcorps.example

https://protoboardly.example/7a2d91e4/screen/58217046

```html
<!DOCTYPE html>
<html lang="en">
<head>
<meta charset="utf-8">
<title>Wheels For Heroes – Donate Your Car</title>
<link href="https://fonts.googleapis.com/css2?family=Roboto:wght@400;500;700;900&display=swap" rel="stylesheet">
<style>
:root{
  --red:#c8102e;
  --red-dark:#a50d25;
  --navy:#1b2f82;
  --navy-deep:#0d1a4d;
  --ink:#2b2f3a;
  --muted:#5c6270;
  --line:#dfe2e8;
  --paper:#ffffff;
  --mist:#f2f3f6;
}
*{box-sizing:border-box;margin:0;padding:0}
html,body{width:1200px;height:2924px;overflow:hidden}
body{font-family:"Roboto",Arial,sans-serif;color:var(--ink);background:var(--paper);position:relative}
.red{color:var(--red)}
.navy{color:var(--navy)}

/* header + hero */
.hero{position:absolute;left:0;top:0;width:1200px;height:600px}
.hero-photo{position:absolute;inset:0;background:linear-gradient(100deg,#d9d2c8 0%,#b9a894 28%,#8a6f5a 45%,#5b6e8c 62%,#c7cbd4 80%,#e9e9ec 100%)}
.site-header{position:absolute;left:0;top:0;width:1200px;height:92px;background:rgba(13,26,77,.82);display:flex;align-items:center;padding:0 60px 0 120px}
.brand{display:flex;align-items:center;gap:12px;color:#fff;font-weight:700;font-size:24px;letter-spacing:.5px}
.brand-mark{width:22px;height:22px;background:var(--red)}
.main-nav{display:flex;gap:40px;margin-left:80px}
.main-nav a{color:#fff;text-decoration:none;font-size:15px;font-weight:500;letter-spacing:.5px;text-transform:uppercase}
.header-contact{margin-left:auto;text-align:right;color:#fff}
.header-phone{font-size:30px;font-weight:700;letter-spacing:.5px}
.header-note{font-size:12px;opacity:.85;margin-top:2px}
.header-cta{display:inline-block;margin-top:8px;background:var(--red);color:#fff;font-size:13px;font-weight:700;padding:7px 16px;text-transform:uppercase}
.header-block{display:flex;flex-direction:column;align-items:flex-end;padding-top:4px}

.donate-form{position:absolute;left:820px;top:112px;width:340px;height:460px;background:var(--paper);box-shadow:0 6px 24px rgba(0,0,0,.25);padding:26px 24px}
.donate-form h2{font-size:26px;font-weight:900;color:var(--navy);text-transform:uppercase;text-align:center;line-height:1.1}
.donate-form .sub{font-size:15px;font-weight:700;color:var(--red);text-align:center;margin:8px 0 20px}
.form-grid{display:grid;grid-template-columns:1fr 1fr;gap:12px}
.field{height:42px;border:1px solid var(--line);background:#fafbfc;font-size:13px;color:var(--muted);display:flex;align-items:center;padding:0 12px;justify-content:space-between}
.field.wide{grid-column:1/3}
.caret{width:0;height:0;border-left:5px solid transparent;border-right:5px solid transparent;border-top:6px solid var(--muted)}
.form-submit{margin-top:18px;height:48px;background:var(--red);color:#fff;font-weight:900;font-size:17px;display:flex;align-items:center;justify-content:center;letter-spacing:.5px}

/* benefits */
.benefits-title{position:absolute;top:600px;left:0;width:1200px;height:112px;display:flex;align-items:center;justify-content:center;font-size:38px;font-weight:900;text-transform:uppercase}
.benefits{position:absolute;top:712px;left:0;width:1200px;height:268px;background:var(--navy)}
.benefits .notch{position:absolute;left:570px;top:0;width:0;height:0;border-left:30px solid transparent;border-right:30px solid transparent;border-top:26px solid var(--paper)}
.benefit-list{position:absolute;left:110px;top:66px;width:980px;display:grid;grid-template-columns:repeat(6,1fr);text-align:center;color:#fff}
.benefit svg{width:64px;height:64px;stroke:#fff;fill:none;stroke-width:2.5;stroke-linecap:round;stroke-linejoin:round}
.benefit p{font-size:15px;margin-top:16px;line-height:1.35;font-weight:500}

/* how */
.how{position:absolute;top:980px;left:0;width:1200px;height:440px;background:var(--paper)}
.how-photo{position:absolute;left:0;top:0;width:500px;height:440px;background:linear-gradient(120deg,#9a2f36 0%,#d9d4cf 30%,#6a5143 55%,#4d5a3e 75%,#c9b69c 100%)}
.how-body{position:absolute;left:560px;top:50px;width:560px}
.how-body h2{font-size:40px;font-weight:900;text-transform:uppercase;margin-bottom:30px}
.step{display:flex;gap:22px;margin-bottom:26px}
.step svg{flex:none;width:40px;height:40px;stroke:var(--red);fill:none;stroke-width:2.5;stroke-linecap:round;stroke-linejoin:round}
.step h3{font-size:16px;font-weight:700;color:var(--red);text-transform:uppercase;margin-bottom:6px}
.step p{font-size:14px;color:var(--muted);line-height:1.5}

/* why */
.why{position:absolute;top:1420px;left:0;width:1200px;height:420px;background:var(--paper);border-top:1px solid var(--line)}
.why h2{text-align:center;font-size:40px;font-weight:900;text-transform:uppercase;margin-top:50px}
.why-cols{position:absolute;left:110px;top:150px;width:980px;display:grid;grid-template-columns:1fr 1fr;gap:0 60px}
.why-item{display:flex;gap:14px;margin-bottom:24px;font-size:14px;line-height:1.55;color:var(--muted)}
.why-item b{color:var(--ink)}
.dot{flex:none;width:16px;height:16px;border-radius:50%;background:var(--red);margin-top:3px}

/* faq */
.faq{position:absolute;top:1840px;left:0;width:1200px;height:460px;background:var(--mist)}
.faq-body{position:absolute;left:110px;top:40px;width:560px}
.faq-body h2{font-size:38px;font-weight:900;text-transform:uppercase;margin-bottom:22px}
.faq-item{display:flex;justify-content:space-between;align-items:center;height:44px;border-bottom:1px solid var(--line);font-size:14px;color:var(--ink)}
.faq-item .plus{color:var(--navy);font-weight:700;font-size:20px}
.faq-photo{position:absolute;left:700px;top:0;width:500px;height:460px;background:linear-gradient(180deg,#5a3a32 0%,#c1673a 40%,#f1b862 62%,#8a4a30 85%,#3b2622 100%)}

/* call */
.call{position:absolute;top:2300px;left:0;width:1200px;height:320px;text-align:center;background:var(--paper)}
.call .kicker{margin-top:26px;font-size:20px;font-weight:700;color:var(--red);text-transform:uppercase}
.call .phone{display:flex;align-items:center;justify-content:center;gap:14px;font-size:46px;font-weight:900;color:var(--navy);margin-top:8px}
.call .phone svg{width:40px;height:40px;fill:var(--navy)}
.call .note{font-size:15px;color:var(--red);margin-top:6px}
.call-flag{width:110px;height:110px;margin:28px auto 0;background:linear-gradient(160deg,#2b3f8f 0%,#2b3f8f 40%,#d33a46 41%,#f1f1f1 70%,#c8102e 100%)}

/* footer */
.site-footer{position:absolute;top:2620px;left:0;width:1200px;height:260px;background:var(--navy-deep);color:#fff}
.footer-brand{position:absolute;left:120px;top:40px;width:380px}
.footer-brand p{font-size:13px;line-height:1.6;opacity:.85;margin-top:20px}
.footer-nav{position:absolute;left:600px;top:40px}
.site-footer h4{font-size:14px;font-weight:700;text-transform:uppercase;letter-spacing:.5px;margin-bottom:16px}
.footer-nav a{display:block;color:#fff;opacity:.85;text-decoration:none;font-size:13px;margin-bottom:10px}
.footer-secure{position:absolute;left:860px;top:40px}
.badges{display:flex;gap:16px}
.badge{width:90px;height:40px;background:#fff;border-radius:4px}
.badge.round{width:50px;height:50px;border-radius:50%;background:#e6e8ee}
.legal{position:absolute;top:2880px;left:0;width:1200px;height:44px;background:var(--red);color:#fff;font-size:12px;display:flex;align-items:center;justify-content:center}
.legal span.right{position:absolute;right:40px}
</style>
</head>
<body>

<section class="hero">
  <div class="hero-photo" role="img" aria-label="Smiling veteran in uniform with his wife and daughter in front of an American flag"></div>
  <header class="site-header">
    <div class="brand"><span class="brand-mark"></span>Wheels For Heroes</div>
    <nav class="main-nav"><a href="#how">How To Donate</a><a href="#why">Why Donate</a><a href="#faq">FAQ</a><a href="#about">About</a></nav>
    <div class="header-block header-contact">
      <div class="header-phone">1-800-555-0142</div>
      <div class="header-note">Live Operators Available - 7 Days A Week</div>
      <span class="header-cta">Donate Now</span>
    </div>
  </header>
  <form class="donate-form">
    <h2>Donate Your Car Online</h2>
    <p class="sub">Full Tax Deduction - Running or Not</p>
    <div class="form-grid">
      <div class="field">First Name</div>
      <div class="field">Last Name</div>
      <div class="field">Phone No</div>
      <div class="field">Zip Code</div>
      <div class="field wide">Email Address</div>
      <div class="field">Choose Year <span class="caret"></span></div>
      <div class="field">Choose Make <span class="caret"></span></div>
      <div class="field wide">Vehicle Model</div>
    </div>
    <div class="form-submit">DONATE NOW</div>
  </form>
</section>

<h2 class="benefits-title"><span class="red">Donate&nbsp;</span><span class="navy">Your Car To Veterans Make A Difference</span></h2>

<section class="benefits">
  <span class="notch"></span>
  <div class="benefit-list">
    <div class="benefit">
      <svg viewBox="0 0 64 64"><rect x="16" y="10" width="32" height="44" rx="3"/><circle cx="32" cy="30" r="9"/><path d="M29 30h6M32 27v6"/></svg>
      <p>You have<br>no costs</p>
    </div>
    <div class="benefit">
      <svg viewBox="0 0 64 64"><path d="M4 42h10l6-12h14v12h-10M34 30h12l10 12v6H34"/><circle cx="18" cy="46" r="5"/><circle cx="48" cy="46" r="5"/><path d="M8 42l12-20"/></svg>
      <p>Free towing,<br>running or not</p>
    </div>
    <div class="benefit">
      <svg viewBox="0 0 64 64"><path d="M14 6h28l10 10v42H14z"/><path d="M42 6v10h10M22 26h20M22 34h20M22 42h12"/></svg>
      <p>We issue you an<br>IRS tax receipt</p>
    </div>
    <div class="benefit">
      <svg viewBox="0 0 64 64"><rect x="12" y="10" width="34" height="46" rx="2"/><path d="M20 22h18M20 30h18M20 38h10"/><path d="M40 46l6 6 12-14"/></svg>
      <p>We take care of<br>all paperwork</p>
    </div>
    <div class="benefit">
      <svg viewBox="0 0 64 64"><rect x="10" y="14" width="44" height="36" rx="3"/><path d="M18 26h14M18 34h20M18 42h10"/><path d="M44 24l6 6M50 24l-6 6"/></svg>
      <p>No DMV<br>Hassles</p>
    </div>
    <div class="benefit">
      <svg viewBox="0 0 64 64"><rect x="8" y="18" width="48" height="30" rx="3"/><path d="M8 28h48M40 18v30"/><circle cx="24" cy="38" r="4"/></svg>
      <p>Vacation<br>Voucher</p>
    </div>
  </div>
</section>

<section class="how" id="how">
  <div class="how-photo" role="img" aria-label="Veteran in uniform hugging his young daughter beside an American flag"></div>
  <div class="how-body">
    <h2><span class="red">How&nbsp;</span><span class="navy">To Donate</span></h2>
    <div class="step">
      <svg viewBox="0 0 40 40"><path d="M10 4l6 8-4 4c2 5 6 9 11 11l4-4 8 6-4 6C18 35 5 22 4 8z"/></svg>
      <div><h3>Call us at 1-800-555-0142 or fill out the online form</h3><p>Donating your vehicle is easy and donation is accepted nationwide.</p></div>
    </div>
    <div class="step">
      <svg viewBox="0 0 40 40"><path d="M2 26h6l4-8h10v8h-6M22 18h8l6 8v4H22"/><circle cx="11" cy="29" r="3"/><circle cx="30" cy="29" r="3"/></svg>
      <div><h3>We tow the vehicle</h3><p>Any vehicles are accepted and we will arrange to pick up your vehicle when it is most convenient for you.</p></div>
    </div>
    <div class="step">
      <svg viewBox="0 0 40 40"><path d="M8 4h18l6 6v26H8z"/><path d="M14 18h12M14 24h12M14 30h8"/></svg>
      <div><h3>Tax write off</h3><p>Once the vehicle donation is complete, you will receive your tax deductible vehicle donation receipt.</p></div>
    </div>
  </div>
</section>

<section class="why" id="why">
  <h2><span class="red">Why Donate&nbsp;</span><span class="navy">Your Car To Us</span></h2>
  <div class="why-cols">
    <div>
      <div class="why-item"><span class="dot"></span><p><b>IRS 501(c)3 Approved</b> - Free 24/7 Pickup with No DMV Hassles.</p></div>
      <div class="why-item"><span class="dot"></span><p><b>Free Local Towing</b> - We will pick up your car donation, running or not, when it's most convenient, at home or work.</p></div>
      <div class="why-item"><span class="dot"></span><p><b>Income Tax Deduction</b> - We issue you an IRS tax receipt and get you the highest tax write-off possible.</p></div>
    </div>
    <div>
      <div class="why-item"><span class="dot"></span><p><b>No Paperwork Hassles</b> - We handle everything: DMV and IRS paperwork.</p></div>
      <div class="why-item"><span class="dot"></span><p><b>Car donations help fund programs</b> - And benefit Harbor Home Fund. An IRS 501(c)3 nonprofit organization.</p></div>
      <div class="why-item"><span class="dot"></span><p><b>Schedule a Free Pickup</b> - Complete the form and a representative will call you to arrange a convenient time to pickup your car.</p></div>
    </div>
  </div>
</section>

<section class="faq" id="faq">
  <div class="faq-body">
    <h2><span class="red">Frequently&nbsp;</span><span class="navy">Asked Questions</span></h2>
    <div class="faq-item">What types of vehicles can be donated?<span class="plus">+</span></div>
    <div class="faq-item">What paperwork do I need to donate my vehicle?<span class="plus">+</span></div>
    <div class="faq-item">Is my donated vehicle tax deductible?<span class="plus">+</span></div>
    <div class="faq-item">What if the vehicle is not registered in my name?<span class="plus">+</span></div>
    <div class="faq-item">How much will I receive as a tax deduction for my vehicle?<span class="plus">+</span></div>
    <div class="faq-item">When will I receive my tax receipt?<span class="plus">+</span></div>
    <div class="faq-item">How do I schedule a pick up?<span class="plus">+</span></div>
  </div>
  <div class="faq-photo" role="img" aria-label="Silhouette of a saluting soldier against a sunset sky with a flag"></div>
</section>

<section class="call">
  <p class="kicker">Call Today To Donate</p>
  <p class="phone"><svg viewBox="0 0 40 40"><path d="M10 4l6 8-4 4c2 5 6 9 11 11l4-4 8 6-4 6C18 35 5 22 4 8z"/></svg>1-800-555-0142</p>
  <p class="note">Live Operators Available - 7 Days A Week</p>
  <div class="call-flag" role="img" aria-label="Waving American flag on a pole"></div>
</section>

<footer class="site-footer" id="about">
  <div class="footer-brand">
    <div class="brand"><span class="brand-mark"></span>Wheels For Heroes</div>
    <p>Car donations help fund local programs and benefit Harbor Home Fund, an IRS 501(c)3 nonprofit. Complete the form and a representative will call you to arrange a pickup.</p>
  </div>
  <div class="footer-nav">
    <h4>Navigation</h4>
    <a href="#how">How To Donate</a><a href="#why">Why Donate</a><a href="#faq">FAQ</a><a href="#about">About</a>
  </div>
  <div class="footer-secure">
    <h4>Safe &amp; Secure</h4>
    <div class="badges"><span class="badge"></span><span class="badge round"></span></div>
  </div>
</footer>
<div class="legal">Copyright © 2020 Wheels For Heroes. Privacy Policy. All Rights Reserved.<span class="right">Site Map</span></div>

</body>
</html>
```